HVAC company business card design

We need a business card design for a HVAC company. The design must look professional. Both sides will be used. The total data to be on the business card is
Name
Position
Email
Direct Phone/Moile Phone
Company Contacts /Address, Phone, Fax, web)
All data will be submit once the design is confirmed. For generic purposes use;
Emre Toksoy
Managing Director
+902324815263 (Mobile)
4712 Sokak No: 9 KBSE Yenikent IZMIR TURKEY
Tel: +902324815263 Fax : +902324815269
www.luvon.com.tr

Target Market(s)

HVAC

Industry/Entity Type

Business

Contact Information for Business Card

The total data to be on the business card is
Name
Position
Email
Direct Phone/Moile Phone
Emre Toksoy
Managing Director
+902324815263 (Mobile)
www.luvon.com.tr
The BC will use both sides of the card. The front will include the full logo and the details for the business card holder. The business card can be divided into vertical/horizontal or to a special shape. The common data like the company address/phone/fax should be indicated elsewehere. The back can contain some part or the whole logo and must contain the web address.

Font styles to use
Serif
Sans Serif

Colors
0355a3
cfdfed

Requirements
Should not have
• Please be careful with the fonts, it shouldnt be too small or too big and must not interfere with the logo fonts. If you need to use a curvy shape please do not use as the logo is already curvy or use the curves from the logo (if it looks good, otherwise forget it)
• We are not in favor of pictograms, only if they are perfect use them.

```html
<!DOCTYPE html>
<html lang="en">
<head>
<meta charset="utf-8">
<title>Luvon Business Card</title>
<link href="https://fonts.googleapis.com/css2?family=Didact+Gothic&display=swap" rel="stylesheet">
<style>
  :root {
    --page-bg: #e9ecf1;
    --card-bg: #ffffff;
    --brand-blue: #0355a3;
    --brand-light: #cfdfed;
    --text-grey: #4a4d55;
    --link-blue: #3a67c4;
    --shadow: rgba(20, 30, 50, 0.18);
  }
  * { margin: 0; padding: 0; box-sizing: border-box; }
  html, body {
    width: 1200px;
    height: 1000px;
    overflow: hidden;
    background: var(--page-bg);
    font-family: "Didact Gothic", "Helvetica Neue", Arial, sans-serif;
  }
  .canvas {
    position: relative;
    width: 1200px;
    height: 1000px;
  }
  .card {
    position: absolute;
    width: 520px;
    height: 336px;
    background: var(--card-bg);
    box-shadow: 0 10px 30px var(--shadow);
  }
  .card--front { left: 50px; top: 332px; }
  .card--back  { left: 630px; top: 332px; display: flex; align-items: center; justify-content: center; }

  .brand {
    position: absolute;
    left: 38px;
    top: 78px;
    display: flex;
    align-items: center;
    gap: 10px;
  }
  .brand__dot {
    width: 26px;
    height: 26px;
    border-radius: 50%;
    background: var(--brand-blue);
  }
  .brand__name {
    font-size: 30px;
    color: var(--brand-blue);
    letter-spacing: 1px;
  }

  .holder {
    position: absolute;
    left: 38px;
    bottom: 48px;
  }
  .holder__name {
    font-size: 30px;
    color: var(--text-grey);
    line-height: 1.1;
  }
  .holder__role {
    font-size: 17px;
    color: var(--link-blue);
  }

  .contact {
    position: absolute;
    left: 262px;
    top: 42px;
    font-size: 16px;
    color: var(--text-grey);
    line-height: 1.3;
  }
  .contact__address { margin-bottom: 52px; }
  .contact__web {
    display: block;
    margin-top: 52px;
    color: var(--link-blue);
    text-decoration: none;
    font-size: 15px;
  }

  .back-brand {
    display: flex;
    align-items: center;
    gap: 14px;
  }
  .back-brand__dot {
    width: 40px;
    height: 40px;
    border-radius: 50%;
    background: var(--brand-blue);
  }
  .back-brand__name {
    font-size: 46px;
    color: var(--brand-blue);
    letter-spacing: 2px;
  }
</style>
</head>
<body>
<main class="canvas">
  <section class="card card--front" aria-label="Business card front">
    <div class="brand">
      <span class="brand__dot"></span>
      <span class="brand__name">Luvon</span>
    </div>

    <div class="contact">
      <p class="contact__address">4712 Sokak No: 9 KBSE<br>Yenikent IZMIR TURKEY</p>
      <p class="contact__phone">+902324815263</p>
      <p class="contact__tel">Tel: +902324815263</p>
      <p class="contact__fax">Fax : +902324815269</p>
      <a class="contact__web" href="#">www.luvon.com.tr</a>
    </div>

    <div class="holder">
      <p class="holder__name">Emre Toksoy</p>
      <p class="holder__role">Managing Director</p>
    </div>
  </section>

  <section class="card card--back" aria-label="Business card back">
    <div class="back-brand">
      <span class="back-brand__dot"></span>
      <span class="back-brand__name">Luvon</span>
    </div>
  </section>
</main>
</body>
</html>
```